Beauty Page

**UPDATED Brief**
We are looking for a website for a beauty organisation that targets both MEN & WOMAN. The focus of the company is in four main areas:

- Health
* Naturopathy & Remedial Massage
- Body
* Yoga
* Personal Training
* Massage
- Skin
* Skin care products such as Velmoracine
- Beauty
* Waxing
* Eye Treatments

We have attached the logo, (a sample of the website that I did - based on the book) and the sample of the pdf book
Updates

Dear All,

Thank you for your patience regarding the beauty contest. We were not happy with the designs that were submitted to us. We therefore had the Graphic designer to do the pricelist book to get all the colours for the organisation.

We are now happy to relaunch the contest and invite you all to take a look at the brief, download a sample of the book and the website we designed on what I’m looking for (the website is only a draft so I don’t want you to copy it) and let your creative mind go wild and present some suggestions to us.

Thanks

 

Target Market(s)

Woman & Men age 24 - 60

Industry/Entity Type

It Company

Requirements
Must have
• Use of main colours
Black
White
Gray - (CYMK - 65, 58, 57, 37)
Purpleish - Maroon (CYMK - 52, 69, 47, 25)

Use of the three color dots on the page.
(white, maroon & Gray)
Same fonts as the book
- Helvetica LT Std
Should not have
• Logo must not be altered i.e different colours, fonts, shadows etc...

```html
<!DOCTYPE html>
<html lang="en">
<head>
<meta charset="utf-8">
<title>Lumavera – Health, Body and Skin Care Centre</title>
<link rel="stylesheet" href="https://fonts.googleapis.com/css2?family=Arimo:wght@400;700&family=Open+Sans:wght@300;400&display=swap">
<style>
:root{
  --maroon:#5c3c4f;
  --maroon-dark:#4a2f40;
  --bg:#6a4a5d;
  --frame:#7d5d70;
  --gray:#4b4b4b;
  --text:#8a8a8a;
  --heading:#2e2e2e;
  --white:#ffffff;
}
*{margin:0;padding:0;box-sizing:border-box}
html,body{width:1049px;height:1200px;overflow:hidden}
body{
  position:relative;
  background:var(--bg);
  background-image:repeating-linear-gradient(45deg,rgba(0,0,0,.05) 0 2px,transparent 2px 5px),
                   repeating-linear-gradient(-45deg,rgba(0,0,0,.05) 0 2px,transparent 2px 5px);
  font-family:Arimo,Arial,sans-serif;
}
.abs{position:absolute}
.header-frame{left:80px;top:0;width:872px;height:160px;background:var(--frame);box-shadow:0 2px 6px rgba(0,0,0,.35)}
.header{left:92px;top:0;width:848px;height:150px;background:var(--white)}
.brand{left:120px;top:30px;font-family:Arimo,Arial,sans-serif;font-weight:700;font-size:56px;letter-spacing:-1px;color:#111;line-height:1}
.tagline{left:120px;top:97px;font-family:"Open Sans",Arial,sans-serif;font-size:19px;color:#111}
.swatches{left:826px;top:16px}
.nav{left:481px;top:100px;width:449px;height:39px;border-radius:4px;
  background:linear-gradient(#6a4a5d,var(--maroon-dark));display:flex;align-items:center;justify-content:space-around;padding:0 8px}
.nav a{color:#fff;text-decoration:none;font-size:14px;font-family:Arial,sans-serif}
.main-frame{left:79px;top:162px;width:874px;height:1018px;background:var(--frame);box-shadow:0 3px 8px rgba(0,0,0,.4)}
.main{left:94px;top:177px;width:845px;height:934px;background:var(--white)}
.hero{left:112px;top:193px;width:808px;height:269px;
  background:linear-gradient(90deg,#a9cbe8 0%,#d8e6f1 35%,#e9d9cc 55%,#f0ece6 75%,#c9a77a 100%)}
.hero-sub{left:128px;top:236px;font-family:"Open Sans",Arial,sans-serif;font-weight:300;font-size:20px;line-height:26px;color:#333}
.hero-title{left:126px;top:395px;font-family:"Open Sans",Arial,sans-serif;font-weight:300;font-size:38px;color:#444}
.pager{left:827px;top:469px;display:flex;gap:5px}
.pager span{width:15px;height:15px;border-radius:50%;background:#d4d4d4;border:1px solid #c4c4c4}
.pager span.on{background:var(--maroon);border-color:var(--maroon-dark)}
.welcome-photo{left:119px;top:526px;width:162px;height:215px;border:2px solid #e4e4e4;background:linear-gradient(#d9b8a0,#f0d6c6 50%,#e9e4e2)}
.flower{left:312px;top:522px}
h2{font-weight:400;color:var(--heading);position:absolute}
.welcome-title{left:362px;top:527px;font-size:24px;font-family:Arial,sans-serif}
.copy{font-size:12px;line-height:15.7px;color:var(--text);font-family:Arial,sans-serif}
.welcome-copy{left:316px;top:570px;width:596px}
.welcome-copy p{margin-bottom:8px}
.btn{position:absolute;background:var(--maroon);color:#fff;font-size:13px;font-family:Arial,sans-serif;text-align:center;border:1px solid var(--maroon-dark);box-shadow:0 1px 2px rgba(0,0,0,.3)}
.btn-read{left:319px;top:712px;width:92px;height:22px;line-height:20px}
.col-title{font-size:20px;font-family:Arial,sans-serif;top:796px}
.news-title{left:129px}
.prod-title{left:398px}
.event-title{left:680px}
.news-copy{left:129px;top:840px;width:250px}
.field{left:129px;top:902px;width:224px;height:27px;border:1px solid #c8c8c8;border-radius:4px;background:linear-gradient(#eee,#f7f7f7)}
.btn-sub{left:197px;top:938px;width:92px;height:24px;line-height:22px;font-size:14px}
.social{left:129px;top:1003px;display:flex;gap:13px}
.social span{width:33px;height:33px;border-radius:50%;box-shadow:0 2px 3px rgba(0,0,0,.3)}
.prod-photo{left:398px;top:831px;width:248px;height:135px;border:1px solid #ddd;background:linear-gradient(120deg,#f1d9a8,#e7b03b 45%,#f6e8c9 70%,#ead6b9)}
.prod-copy{left:398px;top:976px;width:250px}
.btn-more{height:24px;line-height:22px;font-size:14px;width:92px}
.btn-prod{left:558px;top:1037px}
.btn-event{left:808px;top:1037px}
.event-copy{left:680px;top:837px;width:225px}
.event-copy p{margin-bottom:15px}
.footer{left:0;top:1134px;width:1036px;text-align:center;color:#fff;font-size:13px;font-family:Arial,sans-serif}
</style>
</head>
<body>
<div class="abs header-frame"></div>
<header class="abs header"></header>
<div class="abs brand">LUMAVERA</div>
<div class="abs tagline">Health, Body and Skin Care Centre</div>
<svg class="abs swatches" width="100" height="34" viewBox="0 0 100 34">
  <circle cx="16" cy="16" r="14.5" fill="#fff" stroke="#222" stroke-width="1.2"/>
  <circle cx="49" cy="16" r="15" fill="#6a4a5d"/>
  <circle cx="82" cy="16" r="15" fill="#4b4b4b"/>
</svg>
<nav class="abs nav">
  <a href="#">Home</a><a href="#">Health</a><a href="#">Body</a><a href="#">Skin</a><a href="#">Beauty</a><a href="#">Contact us</a>
</nav>

<div class="abs main-frame"></div>
<main class="abs main"></main>

<div class="abs hero" role="img" aria-label="Relaxed woman resting on a white towel beside white orchids on bamboo, blue sky behind"></div>
<div class="abs hero-sub">Lorem ipsum dolor sit amet,<br>consectetur adipisicing elit, sed</div>
<div class="abs hero-title">Lorem ipsum dolor sit amet</div>
<div class="abs pager"><span class="on"></span><span></span><span></span><span></span><span></span></div>

<div class="abs welcome-photo" role="img" aria-label="Facial massage treatment photo"></div>
<svg class="abs flower" width="40" height="40" viewBox="0 0 40 40" aria-hidden="true">
  <g fill="#f4f1e6" stroke="#e0dccb">
    <ellipse cx="20" cy="10" rx="6" ry="9"/>
    <ellipse cx="30" cy="18" rx="9" ry="6"/>
    <ellipse cx="25" cy="30" rx="6" ry="8"/>
    <ellipse cx="13" cy="29" rx="6" ry="8"/>
    <ellipse cx="10" cy="17" rx="9" ry="6"/>
  </g>
  <circle cx="20" cy="20" r="4" fill="#f2c94c"/>
</svg>
<h2 class="welcome-title">Welcome to Our Site</h2>
<div class="abs copy welcome-copy">
  <p>Lorem ipsum dolor sit amet, consectetur adipisicing elit, sed do eiusmod tempor incididunt ut labore et dolore magna aliqua. Ut enim ad minim veniam, quis nostrud exercitation ullamco laboris nisi ut aliquip ex ea commodo consequat.&nbsp; Ut enim ad minim veniam, quis nostrud exercitation ullamco laboris nisi ut aliquip ex ea commodo consequat.</p>
  <p>Lorem ipsum dolor sit amet, consectetur adipisicing elit, sed do eiusmod tempor incididunt ut labore et dolore magna aliqua. Ut enim ad minim veniam, quis nostrud exercitation ullamco laboris nisi ut aliquip ex ea commodo consequat.</p>
</div>
<div class="btn btn-read">Read More...</div>

<h2 class="col-title news-title">Newsletter</h2>
<div class="abs copy news-copy">Lorem ipsum dolor sit amet, consectetur adipisicing elit, sed do eiusmod tempor incididunt ut labore et dolore magna aliqua....</div>
<div class="abs field"></div>
<div class="btn btn-sub">Subscribe</div>
<div class="abs social">
  <span style="background:#2f6fb0"></span>
  <span style="background:#47b3df"></span>
  <span style="background:#e8752b"></span>
  <span style="background:#3a8fa8"></span>
</div>

<h2 class="col-title prod-title">Products &amp; Services</h2>
<div class="abs prod-photo" role="img" aria-label="Spa products: oils, honey, sponge and candle"></div>
<div class="abs copy prod-copy">Lorem ipsum dolor sit amet, consectetur adipisicing elit, sed do eiusmod tempor incididunt ut labore et dolore magna aliqua....</div>
<div class="btn btn-more btn-prod">Read more</div>

<h2 class="col-title event-title">Special Events</h2>
<div class="abs copy event-copy">
  <p>Lorem ipsum dolor sit amet, consectetur adipisicing elit, sed do eiusmod tempor incididunt ut labore et aliqua....</p>
  <p>Lorem ipsum dolor sit amet, consectetur adipisicing elit, sed do eiusmod tempor incididunt ut labore et aliqua....</p>
  <p>Lorem ipsum dolor sit amet, consectetur adipisicing elit, sed do eiusmod tempor incididunt ut labore et aliqua....</p>
</div>
<div class="btn btn-more btn-event">Read more</div>

<footer class="abs footer">Copyright @ 2011. Lumavera.com. All Rights Reserved.</footer>
</body>
</html>
```